Cyber Security Site Design (Products & Consulting)

I need my website redesigned to be engaging, clean, efficient and modern. My company (when its up and running) is going to be concentrated on two things: a few specific products for cyber security as well as cyber security consulting services. The background I bring to the field is having worked with small companies all the way to the largest government organizations and advising them on their security posture and how to improve it. We need the ability to add products and services easily.

For a sample product, you can use either Tarnel (http://www.tarnel-relay.org/) or Vornidex Graywell (https://www.vornidex.com/products/relay-kx-and-enhanced-safe-portal).

It will replace https://dalmorenvue.com/

Target Market(s)

Cyber Security professionals in all verticals

Coding

Coded - Design and coding required

Number of Pages Required

4 page

Font styles to use
Sans Serif

Colors
6b449b

Requirements
Must have
• Ability to easily modify
• Have main page
• Have product specific pages
• Have consulting services pages
• Have executive team information
• Clean, modern design
• Usage of the logo and its color scheme
Nice to have
• I like the idea of a left collapsed sidebar (so icons only) that can expand for text.
• I am also open to a very unique landing page, possibly a shape in the middle (hexagons maybe?) with each of the options there.
Should not have
• Nothing that looks like it came out of a hacker movie

```html
<!DOCTYPE html>
<html lang="en">
<head>
<meta charset="utf-8">
<title>Dalmoren Vue, LLC. — Cyber Security</title>
<link rel="stylesheet" href="https://fonts.googleapis.com/css2?family=Open+Sans:wght@300;400;600;700;800&display=swap">
<style>
:root{
  --purple:#6b449b;
  --purple-light:#8a63bd;
  --purple-deep:#55347f;
  --ink:#1e1e20;
  --text:#333;
  --muted:#8a8a8a;
  --field:#e9e9e9;
  --paper:#f6f6f6;
  --white:#fff;
}
*{box-sizing:border-box;margin:0;padding:0}
html,body{width:1200px;height:3374px;overflow:hidden}
body{position:relative;font-family:"Open Sans",Arial,sans-serif;color:var(--text);background:var(--paper)}
.abs{position:absolute}
a{color:inherit;text-decoration:none}

/* header */
.site-nav{left:249px;top:22px;width:702px;height:63px;background:var(--white);display:flex;align-items:center;padding:0 14px 0 16px;z-index:5;box-shadow:0 2px 10px rgba(0,0,0,.08)}
.brand{display:flex;align-items:center;gap:8px;font-weight:600;font-size:22px;color:var(--purple);letter-spacing:.5px}
.brand-dot{width:24px;height:24px;border-radius:50%;background:var(--purple)}
.nav-links{margin-left:auto;display:flex;align-items:center;gap:17px;font-size:11px;color:#444}
.nav-links .active{color:var(--purple);font-weight:600}
.btn-nav{background:var(--purple);color:var(--white);font-size:9.5px;font-weight:700;padding:9px 14px;margin-left:6px}

/* hero */
.hero{left:0;top:0;width:1200px;height:1116px;background:var(--ink)}
.hero-title{left:249px;top:183px;font-size:53px;line-height:50px;font-weight:800;color:var(--white)}
.hero-copy{left:249px;top:291px;width:360px;font-size:14px;line-height:19px;color:#f1ebf8}
.btn-outline{display:inline-flex;align-items:center;justify-content:center;background:var(--white);color:var(--purple);font-size:11px;font-weight:700;letter-spacing:.3px}

/* about */
.section-title{font-weight:800;text-transform:uppercase;text-align:center;width:1200px;left:0}
.about-title{top:596px;font-size:29px;color:var(--white)}
.about-text{left:249px;top:670px;width:420px;color:var(--white)}
.about-text h3{font-size:13.5px;font-weight:700;line-height:19px;text-transform:uppercase}
.about-text .lead{font-size:13px;line-height:16.5px;margin-top:8px}
.about-text .small{font-size:9px;line-height:14.5px;color:#bdbdbd;margin-top:10px}

/* services */
.services{left:249px;top:1039px;width:702px;height:448px;background:var(--white);box-shadow:0 4px 22px rgba(0,0,0,.14)}
.services h2{position:absolute;top:30px;width:100%;text-align:center;font-size:28px;font-weight:800;color:var(--purple)}
.service{position:absolute;width:234px;text-align:center}
.service svg{width:70px;height:70px}
.service h4{font-size:10px;font-weight:700;color:#222;margin-top:16px;letter-spacing:.2px}
.service p{font-size:9.5px;line-height:13px;color:var(--muted);margin:8px auto 0;width:180px}
.rule-v{position:absolute;width:1px;background:#e2e2e2}
.rule-h{position:absolute;height:1px;background:#e2e2e2}

/* testimonials */
.testi-title{top:1536px;font-size:28px;color:var(--purple)}
.quote-mark{left:0;width:1200px;top:1582px;text-align:center;font-size:60px;font-weight:800;color:var(--purple);line-height:60px}
.testi-copy{left:335px;top:1630px;width:530px;text-align:center;font-size:11.5px;line-height:15.5px;color:#999}
.testi-name{left:0;width:1200px;top:1703px;text-align:center;font-size:10.5px;font-weight:700;color:var(--purple)}
.testi-role{left:0;width:1200px;top:1721px;text-align:center;font-size:9.5px;font-weight:600;color:#888}
.arrow{width:20px;height:20px}

/* team */
.team{left:0;top:1791px;width:1200px;height:347px;background:var(--purple)}
.team h2{position:absolute;left:249px;top:80px;font-size:29px;font-weight:800;color:var(--white)}
.team .sub{position:absolute;left:250px;top:117px;width:340px;font-size:19.5px;line-height:24px;font-weight:300;color:var(--white)}
.team .copy{position:absolute;left:250px;top:175px;width:340px;font-size:12.5px;line-height:17.5px;color:var(--white)}
.team .name{position:absolute;left:250px;top:254px;font-size:8.5px;font-weight:700;color:var(--white)}
.team .role{position:absolute;left:250px;top:269px;font-size:8.5px;color:#cbb8e3}

/* blogs */
.blogs-title{top:2170px;font-size:28px;color:var(--purple)}
.blogs-sub{left:0;width:1200px;top:2217px;text-align:center;font-size:13px;line-height:19px;color:#222}
.post{position:absolute;top:2284px;width:219px}
.post .thumb{width:219px;height:210px;background:var(--white);padding:5px;box-shadow:0 1px 6px rgba(0,0,0,.15)}
.post .thumb div{width:100%;height:100%}
.post h5{font-size:11px;line-height:14px;font-weight:700;color:#222;margin-top:17px;padding:0 2px}
.post .date{font-size:8.5px;color:#555;margin-top:12px;padding:0 2px}
.post p{font-size:8.5px;line-height:13.5px;color:#666;margin-top:7px;padding:0 2px}
.post .more{font-size:9px;font-weight:700;color:var(--purple);margin-top:9px;padding:0 2px;display:block}

/* contact */
.contact-title{left:249px;top:2712px;font-size:29px;font-weight:800;color:var(--purple)}
.contact-sub{left:249px;top:2764px;width:290px;font-size:16px;line-height:20px;color:#222}
.contact-copy{left:249px;top:2812px;width:295px;font-size:11px;line-height:14px;color:#888}
.field{background:var(--field);font-size:9.5px;color:#999;padding:12px 17px}
.btn-submit{left:582px;top:2881px;width:107px;height:36px;background:var(--purple);color:var(--white);font-size:11px;font-weight:700;display:flex;align-items:center;justify-content:center}

/* footer */
.footer-shape{left:0;top:2830px;width:1200px;height:544px}
.footer-brand{left:0;width:1200px;top:3054px;display:flex;justify-content:center;align-items:center;gap:9px;font-size:24px;font-weight:600;color:var(--white);letter-spacing:.5px}
.footer-brand .brand-dot{background:var(--white)}
.ghost-word{left:0;width:1200px;top:3222px;text-align:center;font-size:120px;font-weight:800;color:rgba(0,0,0,.06);letter-spacing:4px;line-height:120px}
.fcol{position:absolute;top:3135px;color:var(--white)}
.fcol h6{font-size:11px;font-weight:700;letter-spacing:.2px;margin-bottom:20px}
.fcol ul{list-style:none}
.fcol li{list-style:none;font-size:9.5px;line-height:23.5px}
.quick li{line-height:21.5px}
.quick li::before{content:"»";margin-right:8px}
.tweet{font-size:9.5px;line-height:15px;margin-bottom:12px}
.tweet b{display:block}
.news-input{left:773px;top:3177px;width:175px;height:34px;border:1px solid var(--white);border-radius:17px;font-size:8px;color:var(--white);padding:11px 20px}
.news-send{left:777px;top:3229px;width:92px;height:34px;border-radius:17px;background:var(--white);color:var(--purple);font-size:11px;font-weight:700;display:flex;align-items:center;justify-content:center}
.copyright{left:0;top:3334px;width:1200px;height:40px;background:var(--purple-deep);color:var(--white);font-size:9px;text-align:center;line-height:40px}
</style>
</head>
<body>

<!-- hero & about backdrop -->
<section class="hero abs">
  <svg class="abs" style="left:0;top:0" width="1200" height="600" viewBox="0 0 1200 600">
    <defs>
      <linearGradient id="heroGrad" x1="0" y1="0" x2="1" y2="1">
        <stop offset="0" stop-color="#7a52ad"/>
        <stop offset="1" stop-color="#5d3a8a"/>
      </linearGradient>
    </defs>
    <path role="img" aria-label="Photo of a team collaborating around a desk, tinted purple"
      fill="url(#heroGrad)"
      d="M0,0 H1200 V540 C1050,600 900,470 720,520 C560,565 430,470 280,505 C160,535 80,560 0,530 Z"/>
    <path fill="none" stroke="#b497e0" stroke-width="3"
      d="M1200,540 C1050,600 900,470 720,520 C560,565 430,470 280,505 C160,535 80,560 0,530"/>
  </svg>
</section>

<header class="site-nav abs">
  <div class="brand"><span class="brand-dot"></span>DALMOREN</div>
  <nav class="nav-links">
    <a class="active">Home</a><a>About us</a><a>Services</a><a>Team</a><a>Blog</a>
    <a class="btn-nav">CONTACT US</a>
  </nav>
</header>

<h1 class="hero-title abs">DALMOREN<br>VUE,LLC.</h1>
<p class="hero-copy abs">Dalmoren Vue, LLC. Is a company that takes its roots from the idea of providing appropriate and creative solutions for cyber security operations,</p>
<a class="btn-outline abs" style="left:249px;top:360px;width:107px;height:31px">READ MORE</a>

<!-- about -->
<h2 class="section-title about-title abs">About Us</h2>
<div class="about-text abs">
  <h3>Dalmoren Vue, LLC. is located in the Brakemoor / Tallis Bay area but</h3>
  <p class="lead">are able to work with clients world-wide. Please contact us for any inquires you may have and we will be glad to assist you in any way possible.</p>
  <p class="small">Lorem Ipsum is simply dummy text of the printing and typesetting industry. Lorem Ipsum has been the industry's standard dummy text ever since the 1500s, when an unknown printer took a galley of type and scrambled it to make a type specimen book. It has survived not only five centuries, but also the leap into electronic typesetting, remaining essentially unchanged. It was popularised in the 1960s with the release of Letraset sheets containing Lorem Ipsum passages Lorem Ipsum is simply dummy text of the printing and typesetting industry. Lorem Ipsum has been the industry's standard dummy text ever since the 1500s, when an unknown printer took a galley of type and scrambled it to make a type specimen book. It has survived not only five centuries, but also the leap into electronic typesetting, remaining essentially unchanged.</p>
</div>
<a class="btn-outline abs" style="left:249px;top:917px;width:107px;height:32px">READ MORE</a>

<div class="abs" style="left:719px;top:658px;width:232px;height:311px;background:var(--purple)"></div>
<div class="abs" style="left:693px;top:904px;width:93px;height:79px;background:var(--purple)"></div>
<div class="abs" role="img" aria-label="Portrait of the company founder" style="left:706px;top:675px;width:229px;height:296px;background:linear-gradient(180deg,#f2f2f2 0%,#d9d6dc 60%,#5b5b60 100%)"></div>

<!-- services -->
<section class="services abs">
  <h2>SERVICES</h2>
  <div class="rule-v" style="left:234px;top:145px;height:118px"></div>
  <div class="rule-v" style="left:469px;top:145px;height:118px"></div>
  <div class="rule-h" style="left:40px;top:250px;width:622px"></div>
  <div class="rule-v" style="left:234px;top:250px;height:170px"></div>
  <div class="rule-v" style="left:469px;top:250px;height:170px"></div>

  <div class="service" style="left:0;top:88px">
    <svg viewBox="0 0 70 70" fill="none" stroke="#6b449b" stroke-width="2.2"><rect x="23" y="30" width="24" height="20" rx="2"/><path d="M28 30v-6a7 7 0 0 1 14 0v6"/><circle cx="35" cy="40" r="3"/><circle cx="12" cy="40" r="4"/><circle cx="58" cy="40" r="4"/><circle cx="35" cy="8" r="4"/><circle cx="35" cy="62" r="4"/><path d="M16 40h7M47 40h7M35 12v6M35 50v8"/></svg>
    <h4>LOREM IPSUM IS SIMPLY DUMMY</h4>
    <p>Lorem Ipsum is simply dummy text of the printing and typesetting industry. Lorem Ipsum has been the industry's</p>
  </div>
  <div class="service" style="left:234px;top:88px">
    <svg viewBox="0 0 70 70" fill="none" stroke="#6b449b" stroke-width="2.2"><path d="M35 6l22 8v18c0 15-10 26-22 31C23 58 13 47 13 32V14z"/><path d="M35 12l16 6v14c0 11-7 19-16 23-9-4-16-12-16-23V18z"/><path d="M26 34l6 6 12-13"/></svg>
    <h4>LOREM IPSUM IS SIMPLY DUMMY</h4>
    <p>Lorem Ipsum is simply dummy text of the printing and typesetting industry. Lorem Ipsum has been the industry's</p>
  </div>
  <div class="service" style="left:468px;top:88px">
    <svg viewBox="0 0 70 70" fill="none" stroke="#6b449b" stroke-width="2.2"><rect x="10" y="26" width="40" height="28" rx="2"/><path d="M4 60h52M6 54h48"/><rect x="40" y="16" width="22" height="18" rx="2"/><path d="M44 16v-5a7 7 0 0 1 14 0v5"/><rect x="16" y="40" width="22" height="6"/></svg>
    <h4>LOREM IPSUM IS SIMPLY DUMMY</h4>
    <p>Lorem Ipsum is simply dummy text of the printing and typesetting industry. Lorem Ipsum has been the industry's</p>
  </div>
  <div class="service" style="left:0;top:273px">
    <svg viewBox="0 0 70 70" fill="none" stroke="#6b449b" stroke-width="2.2"><path d="M14 8h30l8 8v40H14z"/><path d="M20 18h18M20 24h24M20 30h24M20 36h14"/><rect x="34" y="40" width="26" height="20" rx="2"/><path d="M42 40v-4h10v4M34 48h26"/></svg>
    <h4>LOREM IPSUM IS SIMPLY DUMMY</h4>
    <p>Lorem Ipsum is simply dummy text of the printing and typesetting industry. Lorem Ipsum has been the industry's</p>
  </div>
  <div class="service" style="left:234px;top:273px">
    <svg viewBox="0 0 70 70" fill="none" stroke="#6b449b" stroke-width="2.2"><circle cx="46" cy="22" r="14"/><circle cx="46" cy="22" r="6"/><path d="M36 32L10 58l5 5 4-4 4 4 4-4-4-4 4-4-4-4"/></svg>
    <h4>LOREM IPSUM IS SIMPLY DUMMY</h4>
    <p>Lorem Ipsum is simply dummy text of the printing and typesetting industry. Lorem Ipsum has been the industry's</p>
  </div>
  <div class="service" style="left:468px;top:273px">
    <svg viewBox="0 0 70 70" fill="none" stroke="#6b449b" stroke-width="2.2"><circle cx="46" cy="22" r="14"/><rect x="40" y="20" width="12" height="9" rx="1"/><path d="M42 20v-3a4 4 0 0 1 8 0v3"/><circle cx="26" cy="34" r="10"/><path d="M10 62c0-10 7-16 16-16s16 6 16 16"/></svg>
    <h4>LOREM IPSUM IS SIMPLY DUMMY</h4>
    <p>Lorem Ipsum is simply dummy text of the printing and typesetting industry. Lorem Ipsum has been the industry's</p>
  </div>
</section>

<!-- testimonials -->
<h2 class="section-title testi-title abs">Testimonials</h2>
<div class="quote-mark abs">”</div>
<svg class="arrow abs" style="left:264px;top:1642px" viewBox="0 0 20 20" fill="none" stroke="#6b449b" stroke-width="1.6"><circle cx="10" cy="10" r="8.5"/><path d="M11.5 6l-4 4 4 4"/></svg>
<svg class="arrow abs" style="left:915px;top:1642px" viewBox="0 0 20 20" fill="none" stroke="#6b449b" stroke-width="1.6"><circle cx="10" cy="10" r="8.5"/><path d="M8.5 6l4 4-4 4"/></svg>
<p class="testi-copy abs">Lorem Ipsum is simply dummy text of the printing and typesetting industry. Lorem Ipsum has been the industry's standard dummy text ever since the 1500s, when an unknown printer took a galley of type and scrambled it to make a type specimen book. It has survived not only five centuries, but also the leap into electronic typesetting, remaining essentially unchanged.</p>
<div class="testi-name abs">MARCUS EDEVANE HOLT</div>
<div class="testi-role abs">Founder &amp; CEO</div>

<!-- team -->
<section class="team abs">
  <h2>OUR TEAM</h2>
  <p class="sub">Marcus has been in the cyber security fields for over 10 years</p>
  <p class="copy">having worked as a contractor for various Federal agencies. His experiences have provided him the ability to look at the security posture of an organization and provide concise recommendations to improve it's stature.</p>
  <div class="name">MARCUS EDEVANE HOLT</div>
  <div class="role">Founder &amp; CEO</div>
  <div role="img" aria-label="Portrait of the founder in a grey suit" style="position:absolute;left:629px;top:13px;width:322px;height:334px;background:radial-gradient(ellipse at 50% 40%,#9a7cc4 0%,#7d59ad 45%,#4a4a52 100%)"></div>
</section>

<!-- blogs -->
<h2 class="section-title blogs-title abs">Our Blogs</h2>
<p class="blogs-sub abs">Lorem Ipsum is simply dummy text of the printing and<br>typesetting industry. Lorem Ipsum has been the industry's</p>

<article class="post" style="left:249px">
  <div class="thumb"><div role="img" aria-label="Business people shaking hands in an office" style="background:linear-gradient(135deg,#e4e1dc,#8d8a86 60%,#2f3138)"></div></div>
  <h5>LOREM IPSUM IS SIMPLY DUMMY TEXT OF THE PRINTING LOREM IPSUM</h5>
  <div class="date">10 DECEMBER 2018</div>
  <p>Lorem Ipsum is simply dummy text of the printing and typesetting industry. Lorem Ipsum has been the industry's</p>
  <a class="more">READ MORE</a>
</article>
<article class="post" style="left:488px">
  <div class="thumb"><div role="img" aria-label="Glowing digital padlock above an audience" style="background:radial-gradient(circle at 40% 45%,#8fe3ff 0%,#1b78c8 35%,#0b2150 100%)"></div></div>
  <h5>LOREM IPSUM IS SIMPLY DUMMY TEXT OF THE PRINTING LOREM IPSUM</h5>
  <div class="date">10 DECEMBER 2018</div>
  <p>Lorem Ipsum is simply dummy text of the printing and typesetting industry. Lorem Ipsum has been the industry's</p>
  <a class="more">READ MORE</a>
</article>
<article class="post" style="left:729px">
  <div class="thumb"><div role="img" aria-label="Hands typing on a laptop in blue light" style="background:linear-gradient(160deg,#2e7fa0,#0f3f58 50%,#061a26)"></div></div>
  <h5>LOREM IPSUM IS SIMPLY DUMMY TEXT OF THE PRINTING LOREM IPSUM</h5>
  <div class="date">10 DECEMBER 2018</div>
  <p>Lorem Ipsum is simply dummy text of the printing and typesetting industry. Lorem Ipsum has been the industry's</p>
  <a class="more">READ MORE</a>
</article>

<!-- footer shape -->
<svg class="footer-shape abs" viewBox="0 0 1200 544">
  <polygon fill="#7a52ad" points="0,6 419,249 607,150 821,262 1200,39 1200,544 0,544"/>
  <polygon fill="#6b449b" points="0,150 419,249 607,150 821,262 1200,150 1200,544 0,544"/>
  <polyline fill="none" stroke="#4c2d74" stroke-width="3" points="240,140 419,249 607,150 821,262 1000,160"/>
  <circle cx="419" cy="249" r="14" fill="#4c2d74"/>
  <circle cx="607" cy="150" r="14" fill="#a78ccc"/>
  <circle cx="821" cy="262" r="14" fill="#4c2d74"/>
</svg>

<!-- contact -->
<h2 class="contact-title abs">CONTACT US</h2>
<p class="contact-sub abs">Lorem Ipsum is simply dummy text of the printing and typesetting industry.</p>
<p class="contact-copy abs">Lorem Ipsum has been the industry's standard dummy text ever since the 1500s, when an unknown printer took a galley of type and scrambled it to make a type specimen book.</p>
<div class="field abs" style="left:582px;top:2692px;width:178px;height:40px">Name</div>
<div class="field abs" style="left:773px;top:2692px;width:178px;height:40px">Email</div>
<div class="field abs" style="left:582px;top:2746px;width:369px;height:38px">Phone Number</div>
<div class="field abs" style="left:582px;top:2798px;width:369px;height:70px">Messages</div>
<a class="btn-submit abs">SUBMIT</a>

<div class="ghost-word abs">CONTACT US</div>
<div class="footer-brand abs"><span class="brand-dot"></span>DALMOREN</div>

<div class="fcol info" style="left:249px">
  <h6>INFORMATION</h6>
  <ul>
    <li><b>DALMOREN VUE</b></li>
    <li><b>ADDRESS :</b> Abc Street City #1345</li>
    <li><b>EMAIL :</b> info@dalmorenvue.com</li>
    <li><b>PHONE NUMBER :</b> 123 456 789</li>
  </ul>
</div>
<div class="fcol quick" style="left:443px">
  <h6>QUICK LINKS</h6>
  <ul>
    <li>Home</li><li>About us</li><li>Services</li><li>Product</li><li>Blog</li><li>Contact us</li>
  </ul>
</div>
<div class="fcol" style="left:553px;width:190px">
  <h6>LATEST TWEETS</h6>
  <p class="tweet">Lorem Ipsum is simply dummy text of the printing and typesetting<b>17 Hours ago</b></p>
  <p class="tweet">Lorem Ipsum is simply dummy text of the printing and typesetting<b>17 Hours ago</b></p>
</div>
<div class="fcol" style="left:774px">
  <h6>NEWSLETTERS</h6>
</div>
<div class="news-input abs">Your Email Address</div>
<a class="news-send abs">Send</a>

<div class="copyright abs">Copyright @ 2018 <b>Dalmoren Vue, LLC.</b>All Right Reserved</div>

</body>
</html>
```